hi all

Im after a new age looking business card with my company logo on it

must include these details, I would like the PH and Email to be symbols

If the colours used for card could be kept within the colours used in logo that I have supplied that would be great, if another colour is to be used dark grey would be ok. no light bulbs etc thanks

Details below to be incorporated on card

Damian Holloway

Lic E871302

PH 0219647381

E info@brightvaleelectrical.example.nz

Domestic Commercial Industrial Electricians

```html
<!DOCTYPE html>
<html lang="en">
<head>
<meta charset="utf-8">
<title>Brightvale Electrical – Business Card</title>
<link rel="stylesheet" href="https://fonts.googleapis.com/css2?family=Arimo:wght@700&family=Questrial&display=swap">
<style>
  :root {
    --page-bg: #a4a4a4;
    --card-white: #f7f7f7;
    --brand-blue: #2b88d0;
    --ink-dark: #2f2f2f;
    --text-light: #ffffff;
  }
  * { margin: 0; padding: 0; box-sizing: border-box; }
  html, body {
    width: 1200px;
    height: 900px;
    overflow: hidden;
    background: var(--page-bg);
  }
  .canvas {
    position: relative;
    width: 1200px;
    height: 900px;
    display: flex;
    align-items: center;
    justify-content: center;
  }
  .business-card {
    position: relative;
    width: 910px;
    height: 520px;
    background: var(--card-white);
    overflow: hidden;
    box-shadow: 0 14px 34px rgba(0,0,0,0.22);
  }
  .card-split {
    position: absolute;
    inset: 0;
    width: 100%;
    height: 100%;
  }
  .split-blue { fill: var(--brand-blue); }

  .brand-mark {
    position: absolute;
    left: 44px;
    top: 238px;
    display: flex;
    align-items: center;
    gap: 12px;
  }
  .brand-dot {
    width: 28px;
    height: 28px;
    border-radius: 50%;
    background: var(--ink-dark);
    flex: none;
  }
  .brand-name {
    font-family: "Questrial", sans-serif;
    font-size: 27px;
    color: var(--brand-blue);
    letter-spacing: 0.3px;
    white-space: nowrap;
  }

  .contact-side {
    position: absolute;
    inset: 0;
    color: var(--text-light);
  }
  .holder-name {
    position: absolute;
    top: 70px;
    left: 560px;
    font-family: "Arimo", sans-serif;
    font-weight: 700;
    font-size: 34px;
    white-space: nowrap;
  }
  .contact-list {
    position: absolute;
    top: 250px;
    left: 505px;
    list-style: none;
    font-family: "Questrial", sans-serif;
    font-size: 20px;
    line-height: 33px;
  }
  .contact-list li {
    display: flex;
    align-items: center;
    gap: 10px;
    white-space: nowrap;
  }
  .contact-list .licence { padding-left: 36px; }
  .contact-icon {
    width: 26px;
    height: 22px;
    flex: none;
  }
  .contact-icon path,
  .contact-icon rect { fill: none; stroke: var(--text-light); stroke-width: 1.6; }
  .services {
    position: absolute;
    top: 385px;
    left: 478px;
    font-family: "Questrial", sans-serif;
    font-size: 27px;
    line-height: 36px;
    letter-spacing: 0.3px;
    white-space: nowrap;
  }
</style>
</head>
<body>
<main class="canvas">
  <article class="business-card">
    <svg class="card-split" viewBox="0 0 910 520" preserveAspectRatio="none" aria-hidden="true">
      <polygon class="split-blue" points="475,0 910,0 910,520 405,520 492,205 420,205"/>
    </svg>

    <div class="brand-mark">
      <span class="brand-dot" aria-hidden="true"></span>
      <span class="brand-name">Brightvale Electrical</span>
    </div>

    <section class="contact-side">
      <h1 class="holder-name">Damian Holloway</h1>
      <ul class="contact-list">
        <li class="licence">Lic E871302</li>
        <li>
          <svg class="contact-icon" viewBox="0 0 26 22" aria-label="Phone">
            <path d="M8 4 C6 5 5 7 6 10 C7 13 10 16 13 17 C16 18 18 17 19 15 L16 12 L14 14 C12 13 10 11 9 9 L11 7 Z"/>
          </svg>
          <span>0219647381</span>
        </li>
        <li>
          <svg class="contact-icon" viewBox="0 0 26 22" aria-label="Email">
            <rect x="2" y="4" width="22" height="14"/>
            <path d="M2 4 L13 12 L24 4"/>
          </svg>
          <span>info@brightvaleelectrical.example.nz</span>
        </li>
      </ul>
      <p class="services">Domestic Commercial<br>Industrial Electricians Files</p>
    </section>
  </article>
</main>
</body>
</html>
```